Honey Label Design (145 × 55 mm) – Premium / Minimal Style

Project Description
I am looking for a professional label design for a 500 g honey jar (twist-off, copper-colored lid).
The design should look premium, elegant, and minimal, reflecting natural quality and regional authenticity.
I expect two design proposals from each designer:

One concept based strictly on my color and style guidelines
One completely free creative concept (designer's own interpretation)

⚠️ Important: The layout and positioning of all elements must follow my specifications exactly (see below). Creativity is welcome in style, colors, and typography—but not in layout structure and content.

Label Size and Constraints

Final size: 145 mm × 55 mm (landscape)
All elements must remain fully within the label area
No part (especially the hexagon) may extend beyond the label boundaries

Design Style

Minimal, clean, premium
No clutter, no excessive colors
Preferred colors:

Warm natural tones (honey, beige, brown)
Inspired by the branding of: www.wabenhof-laden. de
Subtle copper tone accents (to match the lid)

Background

Very subtle illustrated/sketched background
Motif:

Wildflower meadow (foreground)
Mixed forest (background)

Style should be fine line / sketch style, not photorealistic
The background must remain very soft so text remains clearly readable

Central Element (Mandatory)

A hexagon (honeycomb shape) centered on the label
Inside text:

“GERMAN HONEY”
“500 g”

The hexagon must be:

Fully inside the label (no overlapping, my example is wrong)
Visually balanced and centered

Left Text Block (Important)
The following content (in german) must be placed left-aligned (not centered!):
Bottling point:
Henrik Dollmann Beekeeping
Lindenkamper Weg 17
07318 Saalfeld
Tel.: 03671 5274061
mail@wabenhof-laden.example
Typography must be clean and clearly structured.

Mandatory White Fields (Very Important)
There must be exactly 3 white boxes:
Size:

Each: 28 mm × 12 mm
No visible border

Positioning (must follow exactly):

Bottom center

Completely blank (for honey type)

Right side – upper field

Text above: “Best before:”

Right side – lower field (directly below)

Text above: “Lot number”

⚠️ All three fields must:

Be identical in size
Be perfectly aligned
Match the layout shown in the reference image

Layout Rules (Strict)

The arrangement of elements is fixed and must not be changed
Center field must be directly below the hexagon
Right-side fields must be vertically aligned
Left text must remain left-aligned

goal
The label should communicate:

High quality / premium honey
Regional trust and authenticity
Clean and professional print-ready design

Reference
A reference image is provided showing:

exact placement of all fields
general layout structure

⚠️ The reference is for layout guidance only — not for copying design style.
Updates

All mandatory information must be in German like the address
Bottling point:
Henrik Dollmann Beekeeping
Lindenkamper W. 17
07318 Saalfeld
Tel.: 03671 5274061
www.wabenhof-laden.example

Target Market(s)

Germany

Font styles to use
Sans Serif
Other font styles liked:
• Montserrat, Open Sans, Libre Baskerville

Colors
00AB8E
00BBA5
67D7C9
C6EFE9
E9F9F6
59FF00
82FF00
B8FF75
E3FFCB
F4FFEA
FFF300
FFF600
FEFA6F
FFFEC7
FFFEE8
FFC000
F8CF3A
FAE287
FDF2CF
FEFAEE
F0912C
F2A743
F7CA91
FBE8D2
FDF5EE
EE7325
F08F49
F5BC92
FAE3D3
FDF4ED

Requirements
Must have
• Mandatory Information on Honey Labels (Germany / EU) (Product Name, Country of origin, Net quantity, Minimum durability date (placeholder), Name and address of the food business operator, Batch / lot identification (placeholder), Special warning for infants “Not suitable for infants under 12 months”

```html
<!DOCTYPE html>
<html lang="de">
<head>
<meta charset="utf-8">
<title>German Honey – Etikett 500 g</title>
<link rel="stylesheet" href="https://fonts.googleapis.com/css2?family=Libre+Baskerville:wght@700&family=Nunito+Sans:wght@400;500;700&display=swap">
<style>
  :root {
    --paper: #f8ebd3;
    --paper-deep: #f1dcb8;
    --ink: #3a2716;
    --ink-soft: #4a3522;
    --copper: #b8661a;
    --copper-light: #e0902e;
    --hex-fill: #fbf0dc;
    --field: #ffffff;
    --rule: #c8914a;
  }
  * { margin: 0; padding: 0; box-sizing: border-box; }
  html, body {
    width: 1200px; height: 455px; overflow: hidden;
    background: var(--paper);
  }
  .label {
    position: relative; width: 1200px; height: 455px; overflow: hidden;
    font-family: "Nunito Sans", sans-serif; color: var(--ink);
  }
  .label__scenery {
    position: absolute; inset: 0;
    background:
      linear-gradient(180deg, var(--paper) 0%, #f6e6c9 45%, var(--paper-deep) 100%);
  }
  .label__frame {
    position: absolute; left: 7px; top: 8px; width: 1186px; height: 438px;
    border: 1px solid var(--rule);
  }
  .bottler {
    position: absolute; left: 125px; top: 163px;
    font-size: 16px; line-height: 25.7px; color: var(--ink-soft);
  }
  .bottler__intro { font-size: 16px; margin-bottom: 3px; }
  .bottler__name { font-size: 18px; font-weight: 700; color: var(--ink); margin-bottom: 4px; }
  .bottler__web { font-size: 15.5px; }
  .seal { position: absolute; left: 455px; top: 30px; width: 290px; height: 315px; }
  .seal__text {
    position: absolute; left: 0; right: 0; text-align: center;
    font-family: "Libre Baskerville", serif; font-weight: 700; color: var(--ink);
  }
  .seal__line1 { top: 97px; font-size: 38px; letter-spacing: 4px; }
  .seal__line2 { top: 142px; font-size: 46px; letter-spacing: 4px; }
  .seal__weight { top: 220px; font-size: 27px; color: var(--copper); letter-spacing: 0; }
  .field { position: absolute; background: var(--field); }
  .field--variety { left: 490px; top: 355px; width: 221px; height: 52px; }
  .field--bbd { left: 854px; top: 190px; width: 182px; height: 45px; }
  .field--lot { left: 854px; top: 280px; width: 182px; height: 45px; }
  .field-label {
    position: absolute; left: 858px; font-size: 16px; color: var(--ink-soft);
  }
  .field-label--bbd { top: 162px; }
  .field-label--lot { top: 252px; }
  .warning {
    position: absolute; left: 0; top: 418px; width: 1200px; height: 20px;
  }
  .warning__text {
    position: absolute; left: 441px; top: 0; width: 324px; text-align: center;
    font-size: 13.5px; color: var(--ink-soft); letter-spacing: 0.2px;
  }
</style>
</head>
<body>
<main class="label">
  <div class="label__scenery" role="img" aria-label="Feine Bleistiftzeichnung: Mischwald auf sanften Hügeln im Hintergrund, Wildblumenwiese im Vordergrund, einzelne Bienen"></div>
  <div class="label__frame"></div>

  <address class="bottler" style="font-style:normal">
    <p class="bottler__intro">Abgefüllt von:</p>
    <p class="bottler__name">Imkerei Henrik Dollmann</p>
    <p>Lindenkamper W. 17</p>
    <p>07318 Saalfeld</p>
    <p>Tel.: 03671 5274061</p>
    <p class="bottler__web">www.wabenhof-laden.example</p>
  </address>

  <div class="seal">
    <svg width="290" height="315" viewBox="0 0 290 315" aria-hidden="true">
      <defs>
        <linearGradient id="copperStroke" x1="0" y1="0" x2="1" y2="1">
          <stop offset="0" stop-color="#a9561a"/>
          <stop offset="0.5" stop-color="#e08f30"/>
          <stop offset="1" stop-color="#a9561a"/>
        </linearGradient>
      </defs>
      <polygon points="145,3 286,82 286,233 145,311 4,233 4,82" fill="var(--hex-fill)" stroke="url(#copperStroke)" stroke-width="5"/>
      <polygon points="145,15 276,88 276,227 145,299 14,227 14,88" fill="none" stroke="var(--copper)" stroke-width="1"/>
      <line x1="79" y1="207" x2="139" y2="207" stroke="var(--copper)" stroke-width="1"/>
      <circle cx="145" cy="207" r="2.6" fill="var(--copper)"/>
      <line x1="151" y1="207" x2="212" y2="207" stroke="var(--copper)" stroke-width="1"/>
    </svg>
    <p class="seal__text seal__line1">GERMAN</p>
    <p class="seal__text seal__line2">HONEY</p>
    <p class="seal__text seal__weight">500 g</p>
  </div>

  <div class="field field--variety"></div>
  <p class="field-label field-label--bbd">Mindestens haltbar bis</p>
  <div class="field field--bbd"></div>
  <p class="field-label field-label--lot">Losnummer</p>
  <div class="field field--lot"></div>

  <div class="warning">
    <svg width="1200" height="20" viewBox="0 0 1200 20" aria-hidden="true">
      <line x1="20" y1="10" x2="410" y2="10" stroke="var(--rule)" stroke-width="1"/>
      <circle cx="421" cy="10" r="3" fill="var(--copper)"/>
      <circle cx="783" cy="10" r="3" fill="var(--copper)"/>
      <line x1="795" y1="10" x2="1191" y2="10" stroke="var(--rule)" stroke-width="1"/>
    </svg>
    <p class="warning__text">Nicht geeignet für Säuglinge unter 12 Monaten</p>
  </div>
</main>
</body>
</html>
```